Healthy lifestyle Influencer business card

I need your creativity to have a business card that I can leave in all the restaurants, hotels and spas I visit to inform them that I am an influencer specializing in the wellness sector and that I will write a review about them. You can use my instagram photos Lunavivo27 or on my website www.piattileggerisani.it. I would like my business card to impress with its creativity! thank you very much!

Contact Information for Business Card

siteweb, instagram, phone number

Font styles to use
Decorative
Script

Colors
0094D4
00A9DD
6FCCEA
C7EBF8
E9F6FB
59FF00
82FF00
B8FF75
E3FFCB
F4FFEA
FFC000
F8CF3A
FAE287
FDF2CF
FEFAEE
F0912C
F2A743
F7CA91
FBE8D2
FDF5EE
EE7325
F08F49
F5BC92
FAE3D3
FDF4ED
EB3D1F
EC4F4E
F09395
F8D3D4
FCEDEE
E54698
E96AAD
F1A4CE
F9D9EA
FCEFF6

Requirements
Nice to have
• creativity

```html
<!DOCTYPE html>
<html lang="it">
<head>
<meta charset="utf-8">
<title>Luna Vivo Chef – Business Card</title>
<link rel="stylesheet" href="https://fonts.googleapis.com/css2?family=Montserrat:wght@500;700&display=swap">
<style>
  :root {
    --page-bg: #d8d2cc;
    --ink: #2b2624;
    --ink-soft: #3a3330;
    --peach-light: #ecc9ad;
    --peach-deep: #d6a588;
    --frost-light: #ece9e5;
    --frost-cool: #cdd5db;
    --swoosh: #141212;
    --swoosh-edge: #f4ede6;
    --accent: #b98a5e;
  }
  * { margin: 0; padding: 0; box-sizing: border-box; }
  html, body { width: 1200px; height: 970px; overflow: hidden; }
  body {
    background: var(--page-bg);
    font-family: "Montserrat", Arial, sans-serif;
    color: var(--ink);
  }
  .card {
    position: absolute;
    left: 80px;
    top: 189px;
    width: 1040px;
    height: 592px;
    overflow: hidden;
    box-shadow: 0 12px 40px rgba(0,0,0,0.18);
  }
  .card-bg { position: absolute; inset: 0; width: 100%; height: 100%; }
  .contact {
    position: absolute;
    left: 63px;
    top: 140px;
  }
  .contact-name {
    font-weight: 700;
    font-size: 31px;
    letter-spacing: 0.5px;
    line-height: 1.1;
  }
  .contact-role {
    font-weight: 500;
    font-size: 20px;
    color: var(--ink-soft);
    margin-top: 4px;
  }
  .contact-address {
    font-weight: 500;
    font-size: 20px;
    line-height: 29px;
    color: var(--ink-soft);
    margin-top: 22px;
    font-style: normal;
  }
  .contact-lines {
    list-style: none;
    margin-top: 20px;
  }
  .contact-lines li {
    display: flex;
    align-items: center;
    font-weight: 500;
    font-size: 20px;
    line-height: 30px;
    color: var(--ink-soft);
  }
  .contact-icon {
    width: 18px;
    height: 18px;
    margin-right: 13px;
    flex: none;
  }
  .brand {
    position: absolute;
    left: 520px;
    top: 196px;
    width: 450px;
    text-align: center;
  }
  .brand-name {
    display: inline-flex;
    align-items: center;
    gap: 12px;
    font-weight: 700;
    font-size: 40px;
    color: var(--ink);
  }
  .brand-dot {
    width: 22px;
    height: 22px;
    border-radius: 50%;
    background: var(--accent);
  }
  .brand-tagline {
    font-weight: 500;
    font-size: 17px;
    color: var(--ink);
    margin-top: 14px;
  }
</style>
</head>
<body>
  <section class="card">
    <svg class="card-bg" viewBox="0 0 1040 592" preserveAspectRatio="none" aria-hidden="true">
      <defs>
        <linearGradient id="peachTint" x1="0" y1="0" x2="1" y2="1">
          <stop offset="0" stop-color="var(--peach-light)"/>
          <stop offset="1" stop-color="var(--peach-deep)"/>
        </linearGradient>
        <linearGradient id="frostTint" x1="0" y1="0" x2="1" y2="1">
          <stop offset="0" stop-color="var(--frost-light)"/>
          <stop offset="1" stop-color="var(--frost-cool)"/>
        </linearGradient>
      </defs>
      <rect class="side-warm" width="1040" height="592" fill="url(#peachTint)"/>
      <path class="side-cool" d="M555,0 C460,40 390,110 405,200 C420,330 560,480 665,592 L1040,592 L1040,0 Z" fill="url(#frostTint)"/>
      <path class="heart-swoosh" d="M548,0 C440,38 368,110 378,200 C392,330 530,480 640,592 L665,592 C560,480 420,330 405,200 C390,110 460,40 555,0 Z" fill="var(--swoosh)"/>
      <path class="heart-swoosh-edge" d="M555,0 C460,40 390,110 405,200 C420,330 560,480 665,592" fill="none" stroke="var(--swoosh-edge)" stroke-width="3"/>
    </svg>

    <div class="contact">
      <h1 class="contact-name">MARCO BELLINI</h1>
      <p class="contact-role">President</p>
      <address class="contact-address">2140 Willow Court<br>Fairbanks<br>Alaska 99701</address>
      <ul class="contact-lines">
        <li>
          <svg class="contact-icon" viewBox="0 0 24 24" aria-hidden="true"><path d="M6.6 10.8a15.1 15.1 0 0 0 6.6 6.6l2.2-2.2c.3-.3.7-.4 1-.2 1.1.4 2.3.6 3.6.6.6 0 1 .4 1 1V20c0 .6-.4 1-1 1A17 17 0 0 1 3 4c0-.6.4-1 1-1h3.5c.6 0 1 .4 1 1 0 1.3.2 2.5.6 3.6.1.3 0 .7-.2 1l-2.3 2.2z" fill="var(--ink)"/></svg>
          555.318.2407
        </li>
        <li>
          <svg class="contact-icon" viewBox="0 0 24 24" aria-hidden="true"><rect x="2" y="5" width="20" height="14" rx="1.5" fill="var(--ink)"/><path d="M3 6l9 7 9-7" fill="none" stroke="var(--peach-light)" stroke-width="1.6"/></svg>
          info@piattileggerisani.it
        </li>
        <li>
          <svg class="contact-icon" viewBox="0 0 24 24" aria-hidden="true"><circle cx="12" cy="12" r="10" fill="var(--ink)"/><path d="M2 12h20M12 2c3 3 3 17 0 20M12 2c-3 3-3 17 0 20" fill="none" stroke="var(--peach-light)" stroke-width="1.4"/></svg>
          www.piattileggerisani.it
        </li>
        <li>
          <svg class="contact-icon" viewBox="0 0 24 24" aria-hidden="true"><circle cx="12" cy="12" r="10" fill="var(--ink)"/></svg>
          @Lunavivo27
        </li>
      </ul>
    </div>

    <div class="brand">
      <div class="brand-name"><span class="brand-dot"></span>Luna Vivo Chef</div>
      <p class="brand-tagline">leggeri con i piatti del cuore</p>
    </div>
  </section>
</body>
</html>
```